Platelet Rich Plasma (PRP) Flyer

Hi,

Looking to spruce up our Platelet Rich Plasma Flyer (see power point attachment). I also included previous flyers as examples on the design style we are looking for.

Quorum is our official font of our logo.
Attached is our logo in EPS format.
Please use the current photos in the power point. If you include photos, please make sure the stock image is free.

Files must be under 5MB. JPEG, PNG, PDF, .ai

Thank you,
Marcus

Target Market(s)

Patients

Industry/Entity Type

Healthcare

Font styles to use
Other font styles liked:
• Quorum

Requirements
Must have
• Emphasis on Platelet Rich Plasma Therapy when they pick up the flyer. The price of $199. FSA/HSA Eligible. The different treatment areas. The three addresses. Best of the best logo can be very small, not as important.
Nice to have
• One or two pictures. Less is more
Should not have
• Long paragraphs, multiple sentences.

```html
<!DOCTYPE html>
<html lang="en">
<head>
<meta charset="utf-8">
<title>Platelet Rich Plasma Therapy Flyer</title>
<link href="https://fonts.googleapis.com/css2?family=Montserrat:wght@400;500;600;700&family=Oswald:wght@400;500&family=Quicksand:wght@500;600;700&display=swap" rel="stylesheet">
<style>
  :root{
    --ink:#2b2b2c;
    --ink-deep:#222223;
    --orange:#e8601c;
    --orange-light:#f08a3c;
    --teal:#2fd3b0;
    --teal-dark:#1fae91;
    --cream:#f4ead0;
    --paper:#ffffff;
    --stage:#e6e6e6;
  }
  *{box-sizing:border-box;margin:0;padding:0}
  html,body{width:1200px;height:3005px;overflow:hidden;background:var(--stage)}
  .flyer{position:absolute;left:0;top:652px;width:1200px;height:1700px;overflow:hidden;background:var(--ink);font-family:"Montserrat",sans-serif;color:#fff}
  .flyer-shapes{position:absolute;inset:0;width:1200px;height:1700px}
  .abs{position:absolute}
  .brand{left:40px;top:58px;display:flex;align-items:center;gap:22px}
  .brand-dot{width:70px;height:70px;border-radius:50%;background:var(--teal)}
  .brand-name{font-family:"Quicksand",sans-serif;font-weight:700;font-size:50px;line-height:1;color:var(--orange-light)}
  .brand-web{left:260px;top:150px;font-family:"Quicksand",sans-serif;font-weight:700;font-size:22px;color:var(--orange-light)}
  .title{left:34px;top:212px;font-family:"Quicksand",sans-serif;line-height:.98;color:#fff}
  .title .t1{font-size:48px;font-weight:600}
  .title .t1 b{font-weight:700}
  .title .t2{font-size:74px;font-weight:500}
  .title .t3{font-size:78px;font-weight:700}
  .intro{left:50px;top:522px;width:500px;font-size:17.5px;line-height:23px;text-align:justify;color:#e9e9e9}
  .intro p+p{margin-top:20px}
  .section-tag{left:50px;top:852px;font-family:"Oswald",sans-serif;font-weight:500;font-size:52px;line-height:70px;color:var(--ink-deep)}
  .treat{top:1192px;width:260px;text-align:center;font-weight:700;line-height:1.05;color:#fff}
  .treat small{display:block;font-size:18px;font-weight:600}
  .treat span{display:block;font-size:30px}
  .phone{left:825px;top:948px;font-family:"Oswald",sans-serif;font-size:40px;line-height:1}
  .self-pay{left:880px;top:1040px;font-family:"Oswald",sans-serif;font-weight:500;font-size:42px;line-height:50px;color:var(--ink-deep)}
  .price{left:905px;top:1100px;font-family:"Quicksand",sans-serif;font-weight:700;font-size:92px;line-height:1;color:var(--cream)}
  .per{left:900px;top:1198px;font-weight:700;font-size:24px;line-height:1;color:#fff}
  .fsa{left:900px;top:1230px;font-weight:600;font-size:18px;line-height:1;color:var(--teal)}
  .same-day{left:55px;top:1280px;font-family:"Quicksand",sans-serif;font-weight:700;font-size:68px;line-height:.98;color:var(--teal)}
  .same-day .light{font-weight:500}
  .saturday{left:65px;top:1423px;font-size:23px;line-height:30px;font-weight:700;color:#fff}
  .saturday em{font-style:normal;font-weight:500}
  .on-call{left:560px;top:1316px;width:390px;text-align:center;white-space:nowrap;font-family:"Oswald",sans-serif;font-style:italic;font-weight:500;font-size:48px;line-height:56px;color:var(--ink-deep)}
  .hospital{left:965px;top:1315px;width:230px;text-align:center;font-family:"Quicksand",sans-serif;font-weight:700;color:#fff;line-height:1}
  .hospital .big{font-size:72px}
  .hospital .small{font-size:38px;margin-top:8px}
  .web{left:385px;top:1466px;width:430px;text-align:center;font-size:30px;font-weight:500;line-height:38px;color:#fff}
  .services{left:209px;top:1533px;width:780px;text-align:center;font-size:21px;line-height:24px;font-style:italic;font-weight:500;color:#fff}
  .office{top:1585px;font-size:17px;line-height:21px;color:var(--ink)}
  .office h3{display:flex;align-items:center;gap:8px;font-size:23px;font-weight:700;color:var(--orange);margin-bottom:2px}
  .office p{padding-left:30px}
</style>
</head>
<body>
<main class="flyer">
  <svg class="flyer-shapes" viewBox="0 0 1200 1700">
    <defs>
      <linearGradient id="gold" x1="0" y1="0" x2="1" y2="1">
        <stop offset="0" stop-color="#f7df8a"/>
        <stop offset=".5" stop-color="#d9a93a"/>
        <stop offset="1" stop-color="#f3d57a"/>
      </linearGradient>
      <linearGradient id="lab" x1="0" y1="0" x2="1" y2="1">
        <stop offset="0" stop-color="#e7e3de"/>
        <stop offset=".55" stop-color="#bfc1c6"/>
        <stop offset="1" stop-color="#3d4f7a"/>
      </linearGradient>
      <radialGradient id="knee" cx=".5" cy=".5" r=".6">
        <stop offset="0" stop-color="#8a5a48"/>
        <stop offset="1" stop-color="#1d3a58"/>
      </radialGradient>
    </defs>
    <!-- title block -->
    <rect x="0" y="197" width="620" height="310" fill="var(--orange)"/>
    <!-- photo rings -->
    <circle cx="935" cy="475" r="350" fill="var(--teal)"/>
    <circle cx="915" cy="450" r="335" fill="var(--orange)"/>
    <circle cx="915" cy="454" r="315" fill="url(#lab)" role="img" aria-label="Gloved hands placing blood sample tubes into a centrifuge"/>
    <circle cx="758" cy="756" r="175" fill="var(--teal)"/>
    <circle cx="758" cy="756" r="160" fill="url(#knee)" role="img" aria-label="Person holding a painful knee"/>
    <!-- we are treating tag -->
    <path d="M0 849 H410 a38 38 0 0 1 0 76 H0 Z" fill="var(--teal)"/>
    <line x1="448" y1="887" x2="700" y2="887" stroke="var(--teal)" stroke-width="3"/>
    <!-- treatment icons -->
    <g stroke="var(--teal)" stroke-width="7">
      <circle cx="171" cy="1065" r="100" fill="url(#gold)" role="img" aria-label="Foot sole pain icon"/>
      <circle cx="441" cy="1065" r="100" fill="url(#gold)" role="img" aria-label="Heel and ankle pain icon"/>
      <circle cx="721" cy="1065" r="100" fill="url(#gold)" role="img" aria-label="Knee joint pain icon"/>
    </g>
    <!-- phone icon -->
    <path d="M800 955 c-6 10 2 26 14 34 l6-6 -8-8 -4 3 c-4-3-7-8-8-12 l4-2 -4-11 Z" fill="var(--orange)"/>
    <!-- self pay band -->
    <path d="M870 1033 H1200 V1096 H870 a10 10 0 0 1 -10 -10 V1043 a10 10 0 0 1 10-10Z" fill="var(--teal)"/>
    <!-- divider -->
    <line x1="0" y1="1265" x2="1200" y2="1265" stroke="var(--teal)" stroke-width="3"/>
    <!-- saturday bar -->
    <rect x="50" y="1420" width="440" height="36" rx="6" fill="var(--orange)"/>
    <!-- on call pill -->
    <path d="M1000 1285 H620 a88 88 0 0 0 0 176 H1000 Z" fill="var(--teal)"/>
    <path d="M980 1297 H1200 V1462 H960 Z" fill="var(--orange)"/>
    <!-- footer -->
    <rect x="0" y="1512" width="1200" height="188" fill="var(--paper)"/>
    <path d="M385 1458 H815 V1490 a22 22 0 0 1 -22 22 H407 a22 22 0 0 1 -22-22Z" fill="var(--orange)"/>
    <rect x="209" y="1526" width="780" height="38" rx="19" fill="var(--ink)"/>
  </svg>

  <div class="abs brand"><span class="brand-dot"></span><span class="brand-name">RIDGEVIEW<br>FOOT &amp; ANKLE</span></div>
  <div class="abs brand-web">STRIDEWELLFEET.COM</div>

  <h1 class="abs title">
    <div class="t1"><b>PLATELET</b> RICH</div>
    <div class="t2">PLASMA</div>
    <div class="t3">THERAPY</div>
    <div class="t3">(PRP)</div>
  </h1>

  <div class="abs intro">
    <p>Platelet-rich plasma, or PRP is a substance that helps promote healing when injected. The platelets are the component of your own blood that contains special “factors,” or proteins, that help accelerate tissue repair and regeneration. It also contains proteins that support cell growth.</p>
    <p>Injecting the PRP into damaged tissues will stimulate your body to produce new, healthy cells and promote healing. A consultation is required to make sure you qualify.</p>
  </div>

  <h2 class="abs section-tag">WE ARE TREATING</h2>

  <div class="abs treat" style="left:41px"><small>PLANTAR</small><span>FASCIITIS</span></div>
  <div class="abs treat" style="left:311px"><small>ACHILLES</small><span>TENDONITIS</span></div>
  <div class="abs treat" style="left:571px;width:300px"><small>TENDON &amp; LIGAMENT</small><span>INJURIES</span></div>

  <div class="abs phone">(877) 555 - 0142</div>
  <div class="abs self-pay">SELF PAY PRICE:</div>
  <div class="abs price">$199</div>
  <div class="abs per">PER TREATMENT</div>
  <div class="abs fsa">FSA/HSA ELIGIBLE</div>

  <div class="abs same-day">SAME <span class="light">DAY</span><br>EMERGENCY</div>
  <div class="abs saturday">SATURDAY <em>APPOINTMENTS</em></div>

  <div class="abs on-call">OUR DOCTORS ARE<br>ON CALL AT THE</div>
  <div class="abs hospital"><div class="big">RMC</div><div class="small">ER 24/7</div></div>

  <div class="abs web">www.stridewellfeet.com</div>
  <div class="abs services">Podiatry | Foot &amp; Ankle Surgery | Sports Medicine | Wound Care</div>

  <section class="abs office" style="left:33px">
    <h3><svg width="20" height="24" viewBox="0 0 20 24"><path d="M10 1a8 8 0 0 0-8 8c0 6 8 14 8 14s8-8 8-14a8 8 0 0 0-8-8Zm0 11a3 3 0 1 1 0-6 3 3 0 0 1 0 6Z" fill="var(--orange)"/></svg>Ridgeview Office</h3>
    <p>220 Harbor Point Dr. Ste. 110<br>Ridgeview, MD 21700</p>
  </section>
  <section class="abs office" style="left:449px">
    <h3><svg width="20" height="24" viewBox="0 0 20 24"><path d="M10 1a8 8 0 0 0-8 8c0 6 8 14 8 14s8-8 8-14a8 8 0 0 0-8-8Zm0 11a3 3 0 1 1 0-6 3 3 0 0 1 0 6Z" fill="var(--orange)"/></svg>Millbrook Office</h3>
    <p>845 Aspen Crest Blvd. Ste. 205<br>Millbrook, MD 21710</p>
  </section>
  <section class="abs office" style="left:868px">
    <h3><svg width="20" height="24" viewBox="0 0 20 24"><path d="M10 1a8 8 0 0 0-8 8c0 6 8 14 8 14s8-8 8-14a8 8 0 0 0-8-8Zm0 11a3 3 0 1 1 0-6 3 3 0 0 1 0 6Z" fill="var(--orange)"/></svg>Westfield Office</h3>
    <p>58 Cedar Lane<br>Westfield, WV 25400</p>
  </section>
</main>
</body>
</html>
```